Gift voucher for a photo shoot, folding card DIN long (21 x 9.8 cm)

Hello, I'm a professional photographer and need a new design for my gift voucher card for a photo shoot. The design should be applicable to all types of photo shoots (neutral). I prefer a sophisticated design. The folded card should be printed on both sides.
My data should be included: Logo, Address: Wendtholzer Strße 27, 07549 Gera, Email: fotograf@malteburgardt.eu, Website: www.malteburgardt.eu Tel.: 0173 / 4958302
Updates

Please design the folding card in DIN long format (105 x 210 mm, landscape format). The card should open horizontally. Please design the front with the words "Gift voucher for you" and my logo. Please make the logo small – the words "Gift voucher" should be in the foreground.
The colors - use elegant gray with gold or white font color.
The inside should contain the words: Photo shoot for ........ worth .....€, as well as my logo.
My contact details should be on the back.

Target Market(s)

Private customer

Colors

Designer to choose only greyscale colors for use in the design.

Requirements
Must have
• Noble appearance, a gift voucher that one likes to give away, words: Gift voucher for you, photo shoot for ..., worth .......€
Nice to have
• Noble appearance of the gift voucher, a gift voucher that you like to give away
Should not have
• no pictures

```html
<!DOCTYPE html>
<html lang="en">
<head>
<meta charset="utf-8">
<title>Gift Voucher – Malte Burgardt Fotograf</title>
<link href="https://fonts.googleapis.com/css2?family=Cinzel:wght@400;600&family=Cormorant+Garamond:wght@500&family=Montserrat:wght@400;500&display=swap" rel="stylesheet">
<style>
  :root {
    --backdrop: #ababab;
    --ink: #060708;
    --paper: #ffffff;
    --muted: #a4a4a4;
    --soft: #9a9a9a;
    --contact: #b9b9b9;
    --rule: #4a4a4a;
    --pattern: #f1f1f1;
  }
  * { margin: 0; padding: 0; box-sizing: border-box; }
  html, body { width: 1200px; height: 1200px; overflow: hidden; }
  body { background: var(--backdrop); position: relative; font-family: "Montserrat", sans-serif; }

  .card { position: absolute; left: 99px; width: 1002px; height: 262px; background: var(--paper); }
  .card--outside { top: 296px; }
  .card--inside { top: 648px; }

  /* Outside: back panel */
  .back-panel { position: absolute; left: 0; top: 0; width: 501px; height: 100%; background: var(--ink); }
  .back-mark { position: absolute; left: 187px; top: 17px; }
  .contact-icons { position: absolute; left: 0; width: 100%; top: 166px; display: flex; justify-content: center; align-items: center; gap: 7px; }
  .contact-icons .sep { width: 1px; height: 8px; background: var(--contact); }
  .contact-list { position: absolute; left: 0; width: 100%; top: 182px; list-style: none; text-align: center; color: var(--contact); font-size: 8.5px; line-height: 16.6px; letter-spacing: 0.1px; }

  /* Outside: front panel */
  .front-panel { position: absolute; left: 501px; top: 0; width: 501px; height: 100%; }
  .brand { position: absolute; left: 0; width: 100%; top: 16px; text-align: center; }
  .brand-dot { display: block; margin: 0 auto; }
  .brand-name { font-family: "Cinzel", serif; font-size: 22px; color: var(--ink); letter-spacing: 0.5px; line-height: 1; margin-top: 9px; }
  .brand-role { font-size: 8px; letter-spacing: 3.5px; color: var(--soft); margin-top: 2px; padding-left: 3px; }
  .voucher-title { position: absolute; left: 0; width: 100%; top: 165px; text-align: center; font-family: "Cinzel", serif; font-weight: 600; font-size: 56px; line-height: 1; color: var(--ink); letter-spacing: 0.5px; }
  .voucher-sub { position: absolute; left: 0; width: 100%; top: 221px; text-align: center; font-size: 22px; letter-spacing: 4px; color: var(--muted); font-weight: 500; line-height: 1; }

  /* Inside */
  .inside-band { position: absolute; left: 0; top: 0; width: 100%; height: 131px; background: var(--ink); }
  .shoot-label { position: absolute; left: 31px; top: 46px; font-family: "Cinzel", serif; font-size: 48px; line-height: 1; color: var(--paper); letter-spacing: 0.5px; }
  .worth-tag { position: absolute; left: 652px; top: 46px; width: 194px; height: 42px; display: flex; align-items: center; justify-content: center; }
  .worth-tag::before, .worth-tag::after { content: ""; position: absolute; left: 0; right: 0; height: 1px; background: linear-gradient(90deg, transparent, #9d9d9d 30%, #d0d0d0 50%, #9d9d9d 70%, transparent); }
  .worth-tag::before { top: 0; }
  .worth-tag::after { bottom: 0; }
  .worth-tag span { font-family: "Cinzel", serif; font-weight: 600; font-size: 33px; line-height: 1; color: #a9a9a9; letter-spacing: 0.5px; }

  .texture { position: absolute; top: 131px; height: 131px; background: linear-gradient(180deg, var(--pattern), #f8f8f8); }
  .texture--a { left: 0; width: 151px; }
  .texture--b { left: 351px; width: 302px; }
  .texture--c { left: 854px; width: 148px; }
  .fold { position: absolute; left: 498px; top: 131px; width: 8px; height: 131px; background: linear-gradient(90deg, transparent, rgba(0,0,0,0.04), transparent); }

  .fill-line { position: absolute; top: 222px; border-bottom: 1.5px dotted var(--rule); }
  .fill-line--subject { left: 64px; width: 380px; }
  .fill-line--amount { left: 603px; width: 233px; }
  .currency { position: absolute; left: 834px; top: 140px; font-family: "Cormorant Garamond", serif; font-weight: 500; font-size: 110px; line-height: 1; color: var(--ink); }
</style>
</head>
<body>

<section class="card card--outside">
  <div class="back-panel">
    <svg class="back-mark" width="132" height="132" viewBox="0 0 132 132" aria-hidden="true">
      <circle cx="66" cy="66" r="64" fill="none" stroke="#1c1c1d" stroke-width="2.5"/>
    </svg>
    <div class="contact-icons" aria-hidden="true">
      <svg width="8" height="8" viewBox="0 0 10 10"><path d="M2 1l2 2-1 1.3c.6 1.2 1.5 2.1 2.7 2.7L7 6l2 2-1.3 1.3C4.5 9 1 5.5.7 2.3z" fill="var(--contact)"/></svg>
      <span class="sep"></span>
      <svg width="8" height="8" viewBox="0 0 10 10"><circle cx="5" cy="5" r="4.3" fill="none" stroke="var(--contact)"/><path d="M.7 5h8.6M5 .7c-2.5 2.5-2.5 6.1 0 8.6M5 .7c2.5 2.5 2.5 6.1 0 8.6" fill="none" stroke="var(--contact)" stroke-width=".8"/></svg>
      <span class="sep"></span>
      <svg width="8" height="7" viewBox="0 0 10 8"><rect x=".5" y=".5" width="9" height="7" fill="var(--contact)"/><path d="M.5.5l4.5 4 4.5-4" fill="none" stroke="var(--ink)" stroke-width=".8"/></svg>
      <span class="sep"></span>
      <svg width="8" height="8" viewBox="0 0 10 10"><circle cx="5" cy="3.6" r="2.4" fill="none" stroke="var(--contact)" stroke-width="1.2"/><path d="M1.5 9.5h7M5 6v3" stroke="var(--contact)" stroke-width="1.2"/></svg>
    </div>
    <ul class="contact-list">
      <li>0173 / 4958302</li>
      <li>www.malteburgardt.eu</li>
      <li>fotograf@malteburgardt.eu</li>
      <li>Wendtholzer Strße 27, 07549 Gera</li>
    </ul>
  </div>

  <div class="front-panel">
    <div class="brand">
      <svg class="brand-dot" width="46" height="46" viewBox="0 0 46 46" aria-hidden="true">
        <circle cx="23" cy="23" r="21.5" fill="none" stroke="var(--ink)" stroke-width="2"/>
      </svg>
      <div class="brand-name">Malte Burgardt</div>
      <div class="brand-role">FOTOGRAF</div>
    </div>
    <h1 class="voucher-title">GIFT VOUCHER</h1>
    <p class="voucher-sub">FOR YOU</p>
  </div>
</section>

<section class="card card--inside">
  <div class="inside-band">
    <h2 class="shoot-label">PHOTO SHOOT FOR</h2>
    <div class="worth-tag"><span>WORTH</span></div>
  </div>
  <div class="texture texture--a" role="img" aria-label="Faint repeating monogram pattern"></div>
  <div class="texture texture--b" role="img" aria-label="Faint repeating monogram pattern"></div>
  <div class="texture texture--c" role="img" aria-label="Faint repeating monogram pattern"></div>
  <div class="fold" aria-hidden="true"></div>
  <div class="fill-line fill-line--subject" aria-hidden="true"></div>
  <div class="fill-line fill-line--amount" aria-hidden="true"></div>
  <div class="currency">€</div>
</section>

</body>
</html>
```